Book Cover (HALF OF ALL WORRIES FADE AWAY)

This book is a series of blog posts from my blog, Notes Fit for Borrowing, which is at glenmarwick.com/blog.
The book is to be called:
HALF OF ALL WORRIES FADE AWAY
And 51 other Notes Fit for Borrowing from the Small Business Sage
(Notes Fit for Borrowing) should be italicized.
My name is Glen Marwick, M.B.A.

I will need three variations for my paperback, hardcover and e-book.
Here are some of the blog titles and their topics:
Preparing Your Small Business For Recession small business recession
Should I Incorporate My Business? Should I Incorporate My Business?
Alternative to Minority Shareholder In Small Private Companies minority shareholder
Small Business Culture – Getting it Right Small Business Culture
What is The Right Way to Fire Someone The Right Way to Fire Someone
The Five Basic Leadership Principles Leadership Principles
10 Tips for New Entrepreneurs – Sure Ways to Increase Your Chances of Success
10 things to consider before becoming an entrepreneur
Strategy vs Biz Plans small business strategy
Closing Sales close the sale
Breakeven break even
Growth makes cash flow suck cash flow issues
Think Twice About Offering Early Payment Discounts prepayment discounts
Firing Customers firing customers
Collections best practices getting paid faster
The Cash Flow Statement cash flow statement
Using Paralegals paralegal
Radical Candor radical candor
Why No is the Second Best Word to a Salesperson's ears value of no
The $8 Million Problem -
Contractor vs Employee contractor vs employee
The Vantrell sales tactic
Systems Turn Goals From Dreams Into Reality Systems vs Goals
The Importance of Realistic Goals stretch goals
Why The Owner Must Review Every Hire hiring for values
Systems Thinking for Small Biz: The Case for SOPs systems thinking
Trust Your Gut business intuition
Grease and friction grease vs friction
Left alone, 90% of problems solve themselves strategic inaction
Referrals Are Great—But Not a Growth Strategy referrals
The Lean Marketing Machine: 7 Hacks to Grow Your Small Business Fast marketing hacks
The Small Business Health Check small business health check
How to Spot a Customer Headed for Trouble — Before They Take You Down With Them customer warning signs
We Are What We Repeatedly Do habits
The Smartest People Know When to Play Dumb playing dumb
Before You Scale, Do the Math unit economics
AI for Small Business: Practical Tools and Use Cases AI for Small Business
Title: Tell Me Right Now—Why Can’t We Raise Your Prices? small business pricing
Why Your Real Competitor Isn’t Who You Think creative destruction
Good Enough Might Be Great satisficing
Bootstrapping: Building Your Business on Your Terms bootstrapping
Building Resilient Companies That Never Have to Bet the Farm bet the farm
We Always Overshoot: From Fiber to Cannabis to AI AI overbuild
A Bias Toward Action bias toward ation
Choosing the Right Business Owner Title business owner title
Jobs to Be Done: Understanding What Your Customers Really Want Jobs to Be Done
Forget Money. Here’s What Really Motivates People. motivation

Target Market(s)

Small business operators, business school students

Industry/Entity Type

Small business

Colors

Designer to choose colors to be used in the design.

Requirements
Should not have
• Should not look cartoonish

```html
<!DOCTYPE html>
<html lang="en">
<head>
<meta charset="utf-8">
<title>Half of All Worries Fade Away — Book Cover</title>
<link rel="stylesheet" href="https://fonts.googleapis.com/css2?family=Antonio:wght@700&display=swap">
<style>
  :root {
    --page-bg: #ececec;
    --cover-cyan: #33ddff;
    --cover-glow: #8ff6ff;
    --ink-navy: #334158;
    --title-white: #ffffff;
  }
  * { margin: 0; padding: 0; box-sizing: border-box; }
  html, body {
    width: 1133px;
    height: 1200px;
    overflow: hidden;
    background: var(--page-bg);
  }
  .book-cover {
    position: absolute;
    left: 167px;
    top: 0;
    width: 799px;
    height: 1200px;
    background:
      radial-gradient(ellipse 300px 260px at 50% 62%, var(--cover-glow) 0%, rgba(143,246,255,0) 100%),
      var(--cover-cyan);
    font-family: "Antonio", "Arial Narrow", sans-serif;
    font-weight: 700;
    text-align: center;
  }
  .cover-title {
    position: absolute;
    top: 40px;
    left: 0;
    width: 100%;
    color: var(--title-white);
    font-size: 158px;
    line-height: 160px;
    letter-spacing: -1px;
    text-shadow: 3px 3px 0 var(--ink-navy);
  }
  .cover-title span { display: block; }
  .cover-artwork {
    position: absolute;
    left: 181px;
    top: 690px;
    width: 423px;
    height: 210px;
    border-radius: 6px;
    background: radial-gradient(ellipse at 50% 55%, #4a5a72 0%, var(--ink-navy) 70%);
    opacity: 0.9;
  }
  .cover-subtitle {
    position: absolute;
    top: 918px;
    left: 0;
    width: 100%;
    color: var(--ink-navy);
    font-size: 44px;
    line-height: 52px;
    letter-spacing: -0.5px;
  }
  .cover-subtitle span { display: block; }
  .cover-author {
    position: absolute;
    top: 1072px;
    left: 0;
    width: 100%;
    color: var(--title-white);
    font-size: 72px;
    line-height: 80px;
    letter-spacing: -1px;
    text-shadow: 3px 3px 0 var(--ink-navy);
  }
</style>
</head>
<body>
  <main class="book-cover">
    <h1 class="cover-title">
      <span>HALF OF ALL</span>
      <span>WORRIES</span>
      <span>FADE</span>
      <span>AWAY</span>
    </h1>
    <div class="cover-artwork" role="img" aria-label="Illustration of two dark navy jigsaw puzzle pieces standing side by side"></div>
    <p class="cover-subtitle">
      <span>AND 51 OTHER NOTES FIT FOR BORROWING</span>
      <span>FROM THE SMALL BUSINESS SAGE</span>
    </p>
    <p class="cover-author">Glen Marwick</p>
  </main>
</body>
</html>
```